Global Weight loss program

we need a business card based in Brooklyn , NY called PeppertonRUN . Mara Dulvik Tenbrook the founder and creator of PeppertonRUN Movement. A business based around nutrition, health, Whole Foods and fitness.

Industry/Entity Type

Food Service

Contact Information for Business Card

Phone number : 718-555-0143
website www.peppertonrun.com
email : mara@peppertonrun.com

Font styles to use
Sans Serif

Requirements
Must have
• logo colors
• green black and gold
Nice to have
• must be simple and sharp.
Should not have
• pictures of items

```html
<!DOCTYPE html>
<html lang="en">
<head>
<meta charset="utf-8">
<title>PeppertonRUN Business Card</title>
<link href="https://fonts.googleapis.com/css2?family=Open+Sans:wght@400;600;700&display=swap" rel="stylesheet">
<style>
  :root {
    --page-bg: #e9e6e1;
    --card-dark: #333334;
    --card-light: #f7f7f6;
    --brand-green: #6cbf2a;
    --brand-gold: #c9a227;
    --ink-dark: #3a3a3a;
    --ink-mid: #5c5c5c;
    --ink-light: #ffffff;
    --ghost-tone: #e4e8dc;
  }
  * { margin: 0; padding: 0; box-sizing: border-box; }
  html, body {
    width: 1200px; height: 840px; overflow: hidden;
    background: var(--page-bg);
    font-family: "Open Sans", Arial, sans-serif;
  }
  .canvas { position: relative; width: 1200px; height: 840px; }
  .card {
    position: absolute; left: 290px; width: 620px; height: 354px;
    box-shadow: 0 6px 18px rgba(0,0,0,0.18);
    overflow: hidden;
  }
  .card-front { top: 50px; background: var(--card-dark); }
  .card-back { top: 436px; background: var(--card-light); }

  .front-brand {
    position: absolute; top: 130px; left: 0; right: 0;
    display: flex; align-items: center; justify-content: center; gap: 16px;
  }
  .brand-square { width: 46px; height: 46px; background: var(--brand-gold); }
  .front-brand-name {
    font-size: 40px; font-weight: 700; color: var(--ink-light); letter-spacing: 0.5px;
  }
  .front-roles {
    position: absolute; bottom: 34px; left: 0; right: 0;
    text-align: center; font-size: 13px; color: var(--ink-light); letter-spacing: 0.3px;
  }
  .role-divider { color: var(--brand-gold); }

  .ghost-mark {
    position: absolute; left: 40px; top: 60px; width: 220px; height: 260px;
    background: linear-gradient(160deg, var(--ghost-tone), rgba(228,232,220,0.2));
    opacity: 0.8;
  }
  .back-brand {
    position: absolute; top: 54px; right: 40px;
    display: flex; align-items: flex-start; gap: 12px;
  }
  .back-brand-square { width: 14px; height: 14px; margin-top: 12px; background: var(--brand-gold); }
  .back-brand-name {
    font-size: 34px; font-weight: 600; color: var(--ink-dark); line-height: 1;
  }
  .back-brand-tagline {
    margin-top: 6px; font-size: 11px; color: var(--ink-mid); letter-spacing: 1.5px;
  }
  .contact-block { position: absolute; left: 150px; top: 196px; }
  .person-name {
    font-size: 19px; font-weight: 700; color: var(--brand-green); letter-spacing: 0.5px;
  }
  .person-role { font-size: 14px; color: var(--ink-dark); margin-bottom: 14px; }
  .contact-line { font-size: 13px; color: var(--ink-mid); line-height: 1.55; }
  .contact-label { font-weight: 700; color: var(--brand-green); }
</style>
</head>
<body>
<div class="canvas">
  <section class="card card-front">
    <div class="front-brand">
      <div class="brand-square"></div>
      <div class="front-brand-name">PeppertonRUN</div>
    </div>
    <p class="front-roles">Health Coach <span class="role-divider">|</span> Personal Trainer <span class="role-divider">|</span> Natural Gourmet Chef</p>
  </section>

  <section class="card card-back">
    <div class="ghost-mark" role="img" aria-label="Faint brand emblem decoration"></div>
    <div class="back-brand">
      <div class="back-brand-square"></div>
      <div>
        <div class="back-brand-name">PeppertonRUN</div>
        <div class="back-brand-tagline">Fitness, Nutrition and Health</div>
      </div>
    </div>
    <div class="contact-block">
      <div class="person-name">MARA DULVIK TENBROOK</div>
      <div class="person-role">FOUNDER</div>
      <div class="contact-line"><span class="contact-label">Phone:</span> 718-555-0143</div>
      <div class="contact-line"><span class="contact-label">Email:</span> mara@peppertonrun.com</div>
      <div class="contact-line"><span class="contact-label">Web:</span> www.peppertonrun.com</div>
    </div>
  </section>
</div>
</body>
</html>
```